We are working on a book for our business you helped us design a logo for Title : Bright Path Forward:
Sub Title : Growing your company while keeping your heart
Authors : Martin Corvaux and Owen Trapp

we would like the book cover to be simple and complimentary to the logo but not exactly the same.

```html
<!DOCTYPE html>
<html lang="en">
<head>
<meta charset="UTF-8">
<title>Bright Path Forward — Book Cover</title>
<link href="https://fonts.googleapis.com/css2?family=Bebas+Neue&display=swap" rel="stylesheet">
<style>
  :root {
    --backdrop: #e9e9ea;
    --paper: #ffffff;
    --ink-grey: #5e5e5e;
    --gold-deep: #dcae55;
    --gold-light: #f8e39c;
    --gold-mid: #e8c06c;
  }
  * { margin: 0; padding: 0; box-sizing: border-box; }
  html, body {
    width: 1200px; height: 1200px; overflow: hidden;
    background: var(--backdrop);
  }
  body {
    display: flex; align-items: center; justify-content: center;
    font-family: "Bebas Neue", "Oswald", sans-serif;
  }
  .book-cover {
    position: relative;
    width: 740px; height: 1110px;
    background: var(--paper);
    display: flex; flex-direction: column; align-items: center;
    box-shadow: 0 10px 30px rgba(0,0,0,0.12);
  }
  .authors {
    margin-top: 52px;
    font-size: 56px; letter-spacing: 1px;
    color: var(--ink-grey);
    line-height: 1;
  }
  .gold-text {
    background: linear-gradient(100deg, var(--gold-deep) 0%, var(--gold-mid) 30%, var(--gold-light) 50%, var(--gold-mid) 70%, var(--gold-deep) 100%);
    -webkit-background-clip: text; background-clip: text;
    color: transparent;
  }
  .title-main {
    font-size: 262px; line-height: 0.82;
    margin-top: 22px;
  }
  .title-middle {
    display: flex; align-items: center; gap: 32px;
    margin-top: 4px;
  }
  .title-middle .rule { width: 140px; height: 5px; background: var(--ink-grey); }
  .title-middle .word { font-size: 118px; line-height: 0.9; }
  .title-end {
    font-size: 232px; line-height: 0.82;
    margin-top: 0;
  }
  .imprint-row {
    display: flex; align-items: center; gap: 18px;
    margin-top: 26px;
  }
  .imprint-row .rule { width: 170px; height: 5px; background: var(--ink-grey); }
  .imprint {
    display: flex; align-items: center; gap: 10px;
    color: var(--ink-grey); font-size: 40px; line-height: 1;
  }
  .imprint .dot { width: 22px; height: 22px; border-radius: 50%; background: var(--ink-grey); }
  .subtitle {
    margin-top: 30px;
    text-align: center;
    font-size: 66px; line-height: 0.98;
    color: var(--ink-grey);
  }
  .bottom-rule {
    margin-top: 34px;
    width: 560px; height: 5px; background: var(--ink-grey);
  }
  .gold-band {
    position: absolute; left: 0; bottom: 0;
    width: 100%; height: 108px;
    background: linear-gradient(100deg, var(--gold-deep) 0%, var(--gold-mid) 30%, var(--gold-light) 55%, var(--gold-mid) 75%, var(--gold-deep) 100%);
  }
</style>
</head>
<body>
  <main class="book-cover">
    <p class="authors">Martin Corvaux - Owen Trapp</p>
    <h1 class="title">
      <span class="title-main gold-text" style="display:block;text-align:center;">Bright</span>
      <span class="title-middle">
        <span class="rule"></span>
        <span class="word gold-text">Path</span>
        <span class="rule"></span>
      </span>
      <span class="title-end gold-text" style="display:block;text-align:center;">Forward</span>
    </h1>
    <div class="imprint-row">
      <span class="rule"></span>
      <span class="imprint"><span class="dot"></span>Northwise</span>
      <span class="rule"></span>
    </div>
    <p class="subtitle">Growing your company<br>while keeping your heart</p>
    <div class="bottom-rule"></div>
    <div class="gold-band"></div>
  </main>
</body>
</html>
```